Unique, Impressive, and Modern Business Card

Looking for a distinctive, unique business card. We are distributors of tire repairs supplies, tools, machinery, and chemicals. Our target market are tire repair shops, tire franchises, and mechanic shops. We would like our design to include tire characteristics, and use our business colors. Feel free to use all types design and printing options (emboss, spot uv, foil, etc) QR code may be applied, you can use different size business cards ( standard, square, rounded edge, colored edge, etc), all formats needed for printing, also editable for future changes

Target Market(s)

Automotive, Tire industries

Industry/Entity Type

Tire Industry (automotive)

Contact Information for Business Card

Business logo, business Name (Quillmark Industries Inc), Name (Doran Pellig), Position (President) Address (48 Fernhollow Lane, Brentwood NY 11729), Contact number (Company 1-855-302-4418, Cell 1-631-540-2937, email address (doran.pellig@quillmarkusa.example), URL (www.quillmarkusa.example

Requirements
Must have
• Must include Business Colors (Black, Green, Blue, White) see sample website file
Nice to have
• emboss, spot uv, etc

```html
<!DOCTYPE html>
<html lang="en">
<head>
<meta charset="utf-8">
<title>Quillmark Industries Business Card</title>
<link href="https://fonts.googleapis.com/css2?family=Montserrat:ital,wght@0,400;0,500;0,700;1,700&display=swap" rel="stylesheet">
<style>
  :root {
    --page: #141414;
    --card: #232323;
    --ink: #ffffff;
    --muted: #d8d8d8;
    --blue: #2a3fa0;
    --pattern-dark: #1b1b1b;
    --pattern-light: #4a4a4a;
  }
  * { margin: 0; padding: 0; box-sizing: border-box; }
  html, body { width: 1200px; height: 900px; overflow: hidden; }
  body {
    background: var(--page);
    font-family: "Montserrat", Arial, sans-serif;
    color: var(--ink);
    position: relative;
  }
  .card {
    position: absolute;
    left: 250px;
    width: 700px;
    height: 400px;
    background: var(--card);
    overflow: hidden;
    box-shadow: 0 10px 30px rgba(0,0,0,.6);
  }
  .card-front { top: 40px; }
  .card-back { top: 470px; }

  .brand {
    position: absolute;
    display: flex;
    align-items: center;
    gap: 18px;
  }
  .brand-dot {
    width: 58px; height: 58px;
    border-radius: 50%;
    background: var(--ink);
    flex: none;
  }
  .brand-name {
    font-weight: 500;
    color: var(--ink);
    line-height: 1.1;
    text-transform: uppercase;
  }
  .brand-name .line-main { display: block; font-size: 40px; letter-spacing: 1px; }
  .brand-name .line-sub { display: block; font-size: 14px; letter-spacing: 10px; padding-left: 6px; }
  .card-front .brand { left: 345px; top: 62px; }

  .contact-block { position: absolute; left: 40px; top: 60px; }
  .person-name { font-size: 24px; font-weight: 700; font-style: italic; color: var(--blue); }
  .person-role { font-size: 14px; color: var(--muted); margin-bottom: 14px; }
  .contact-line { display: flex; align-items: center; gap: 10px; font-size: 14px; margin-top: 6px; }
  .contact-line svg { width: 12px; height: 12px; fill: var(--ink); flex: none; }

  .rule { position: absolute; left: 40px; right: 40px; top: 248px; height: 1px; background: var(--blue); }

  .address { position: absolute; right: 40px; top: 262px; text-align: right; font-size: 15px; line-height: 1.4; }
  .bands { position: absolute; left: 0; top: 0; width: 700px; height: 400px; }
  .website { position: absolute; right: 40px; top: 355px; font-size: 15px; color: var(--ink); }

  .pattern-field {
    position: absolute; inset: 0;
    background: linear-gradient(120deg, var(--pattern-dark) 0%, #2a2a2a 55%, var(--pattern-light) 100%);
  }
  .card-back .brand { left: 180px; top: 160px; }
</style>
</head>
<body>

<section class="card card-front">
  <svg class="bands" viewBox="0 0 700 400" aria-hidden="true">
    <path d="M0,350 L300,371 L0,365 Z" fill="#ffffff"/>
    <path d="M0,372 L300,372 C340,372 350,340 400,340 L700,340 L700,400 L0,400 Z" fill="#2a3fa0"/>
  </svg>

  <div class="brand">
    <span class="brand-dot"></span>
    <span class="brand-name"><span class="line-main">Quillmark</span><span class="line-sub">Industries</span></span>
  </div>

  <div class="contact-block">
    <p class="person-name">Doran Pellig</p>
    <p class="person-role">President</p>
    <p class="contact-line">
      <svg viewBox="0 0 12 12"><path d="M2 0h3l1 3-2 1.2a7 7 0 0 0 3.8 3.8L9 6l3 1v3c0 1-1 2-2 2C4.5 12 0 7.5 0 2 0 1 1 0 2 0z"/></svg>
      1-855-302-4418
    </p>
    <p class="contact-line">
      <svg viewBox="0 0 12 12"><path d="M3 0h6a1 1 0 0 1 1 1v10a1 1 0 0 1-1 1H3a1 1 0 0 1-1-1V1a1 1 0 0 1 1-1zm0 2v7h6V2z"/></svg>
      1-555-540-2937
    </p>
    <p class="contact-line">
      <svg viewBox="0 0 12 12"><path d="M0 2h12v1L6 7 0 3zm0 2.5 6 4 6-4V10H0z"/></svg>
      doran.pellig@quillmarkusa.example
    </p>
  </div>

  <div class="rule"></div>

  <p class="address">48 Fernhollow Lane<br>Larkhaven Falls 00417</p>
  <p class="website">www.quillmarkusa.example</p>
</section>

<section class="card card-back">
  <div class="pattern-field" role="img" aria-label="Repeating embossed brand pattern in gloss black and silver tones"></div>
  <div class="brand">
    <span class="brand-dot"></span>
    <span class="brand-name"><span class="line-main">Quillmark</span><span class="line-sub">Industries</span></span>
  </div>
</section>

</body>
</html>
```